New Vidora Channel Banner Graphic/Logo for "Cozy Nook Attic Sound"

Create a banner for my new Vidora channel for Cozy Nook Attic Sound. This is partially a logo project, but the logo will not be used elsewhere. Check out Vidora channels to see the banners others have created. This channel is about my home studio, the gear, microphones, musical instruments, wiring, software etc. that goes into a home studio. It's a free channel, made for sharing information. This is a graphic design that will be posted on vidora using built-in vidora tools.
Updates

More information about this project! I'm staring a channel called "Cozy Nook Attic Sound" on vidorastream.net. I need a deign for this banner and a logo for Cozy Nook Attic Sound. I called the channel by that name because my music studio is my happy place. It's about music and instruments (gutars, piano, drums, percussion) singing (microhpones), creativity, and what you'd expect form musicians. It's also about technology, recording, live-streaming, music videos, etc. It is my hobby, not my profession. I will be creating content for other amateur home studio aficionados and hobbyists. There are a lot of home studio channels and videos you can look at on vidora to get a flavor for musicians and studios. Usually fairly tech-heavy. An appeal of my channel will be a very approachable, "i'm the same as you" welcome for people that are doing it to enjoy it.

I put this project in the wrong category to start. This has been fixed, but I think benefits I would have received (such as invited designers) and announcement of project in the correct category mean I'm not getting designers. Your initial menu should be improved. I'm having a banner created for a web page in Vidora. I think it is easy to mistake that for a web design when it is really a graphic design for the web.

Target Market(s)

Similar to myself, people as interested in studio/production tech as they are in making music, perhaps trending a bit older and successful enough to afford some gear!

Number of Pages Required

1 page

Font styles to use
Sans Serif

Requirements
Must have
• This is not really a web design, i may have miscategorized. Please see uploaded docs for pics of similar banner on a Vidora page. ADDED 1/5: As this is a vidora channel that could be viewed on any device, the banner should be friendly in this way and design or design variations needed for PC, Tabrix, phone vie3wing.

Here are the Vidora size specs:
Banner image guidelines
Your banner image must meet the following criteria:

Minimum dimension for upload: 2048 x 1152 px with an aspect ratio of 16:9.
At the Minimum dimension, the safe area for text and logos: 1235 x 338 px. Larger images may get cropped on certain views or devices.
File size: 6 MB or smaller.
How to resize images

You can use your computer's image editor or an online image resizer to resize the images. For example, you can use Preview on an Quince computer or Microsoft Photos on Windows.

```html
<!DOCTYPE html>
<html lang="en">
<head>
<meta charset="utf-8">
<title>Cozy Nook Attic Sound – Channel Banner</title>
<link rel="stylesheet" href="https://fonts.googleapis.com/css2?family=Poppins:wght@400;600&display=swap">
<style>
  :root {
    --paper-light: #e4e4e4;
    --paper-mid: #cfcfcf;
    --paper-dark: #b9b9b9;
    --wood-light: #b98458;
    --wood-mid: #9a6840;
    --wood-dark: #5a3a22;
    --ink: #ffffff;
  }
  * { margin: 0; padding: 0; box-sizing: border-box; }
  html, body {
    width: 1200px;
    height: 198px;
    overflow: hidden;
    background: var(--paper-mid);
  }
  .banner {
    position: relative;
    width: 1200px;
    height: 198px;
    overflow: hidden;
    font-family: "Poppins", sans-serif;
    color: var(--ink);
    background: linear-gradient(90deg, var(--paper-dark) 0%, var(--paper-light) 38%, var(--paper-mid) 100%);
  }
  .guitar-photo {
    position: absolute;
    inset: 0;
    width: 1200px;
    height: 198px;
  }
  .brand {
    position: absolute;
    left: 250px;
    top: 38px;
    width: 320px;
    text-align: center;
    font-weight: 400;
  }
  .brand-name {
    font-size: 38px;
    line-height: 1.05;
    letter-spacing: 0.5px;
  }
  .brand-name span {
    display: block;
    font-size: 20px;
    letter-spacing: 1px;
    margin-top: 6px;
  }
  .brand-byline {
    font-size: 10px;
    margin-top: 6px;
  }
  .channel-info {
    position: absolute;
    left: 620px;
    top: 56px;
    width: 340px;
    text-align: center;
  }
  .tagline {
    font-size: 11.5px;
    font-weight: 600;
  }
  .topics {
    font-size: 7.5px;
    font-weight: 400;
    margin-top: 12px;
  }
  .follow {
    font-size: 7.5px;
    font-weight: 400;
    margin-top: 11px;
  }
  .contact {
    font-size: 11.5px;
    font-weight: 600;
    margin-top: 9px;
  }
</style>
</head>
<body>
  <div class="banner">
    <svg class="guitar-photo" viewBox="0 0 1200 198" role="img" aria-label="Close-up photo of an acoustic guitar body with its sound hole and strings">
      <defs>
        <linearGradient id="wood" x1="0" y1="0" x2="1" y2="0">
          <stop offset="0" stop-color="var(--wood-light)"/>
          <stop offset="0.55" stop-color="var(--wood-mid)"/>
          <stop offset="1" stop-color="var(--wood-dark)"/>
        </linearGradient>
      </defs>
      <path d="M578 0 C 600 70 622 140 658 198 L1200 198 L1200 0 Z" fill="url(#wood)"/>
    </svg>

    <div class="brand">
      <p class="brand-name">Cozy Nook<span>Attic Sound</span></p>
      <p class="brand-byline">by Dale Whitcomb</p>
    </div>

    <div class="channel-info">
      <p class="tagline">A Regular Joe Blowin' his Dough on Gear &amp; Guitars</p>
      <p class="topics">Music + Gear + Livestreaming + Recording + DAW + Instruments + Vidora</p>
      <p class="follow">Follow my Studio Renovation | Free How-To's</p>
      <p class="contact">CozyNookAtticSound@mailwell.net</p>
    </div>
  </div>
</body>
</html>
```